Buch-/eBook-Cover für ein Rivora PLT Taschenbuch
Zielgruppe
Wald & Stein Verlag ist ein moderner Verlag für islamische Bücher über innere Heilung, Herzruhe und persönliche Entwicklung im Licht des Qurans und der Sunnah. Der Verlag verbindet spirituelle Tiefe mit emotionalen Alltagsthemen wie Overthinking, Angst, Sabr, Tawakkul, Selbstheilung und innerem Frieden.
Aufgabenstellung
Wir benötigen ein modernes! Cover für ein Rivora PLT Taschenbuch in deutscher Sprache.
Titel: Oh je, meine Tage laufen davon weiter
Untertitel: Wie du durch kleine Schritte Halt gewinnst - selbst wenn dein Alltag dich stark fordert
Autorenname: Lotte Brenk
Verlagsname: Wald & Stein Verlag
Nische: Islam + Overthinking
Zielgruppe: Islamische Frauen
Vermarktung: Über Flixo
Es soll ein emotional ansprechendes Cover erstellt werden im modernen Design in deutscher Sprache für die Zielgruppe islamische Frauen.
Cover für Rivora PLT
Maße:
15,24 x 22,86 cm
6 x 9 Zoll
Vorder und Rückseite
E-Book E-Book"
Das Design darf nicht zu überladen sein.

```html
<!DOCTYPE html>
<html lang="de">
<head>
<meta charset="utf-8">
<title>Oh je, meine Tage laufen davon weiter – Lotte Brenk</title>
<link rel="stylesheet" href="https://fonts.googleapis.com/css2?family=Josefin+Sans:wght@400;600;700&display=swap">
<style>
  :root {
    --backdrop: #e4dad9;
    --cover-blue: #4a7a9c;
    --cream: #eadfb4;
    --white: #ffffff;
    --photo-top: #aebfd4;
    --photo-mid: #d4cdd0;
    --photo-low: #e9e2d8;
    --photo-shade: rgba(38, 32, 40, 0.88);
  }
  html, body {
    margin: 0;
    width: 1200px;
    height: 1200px;
    overflow: hidden;
    background: var(--backdrop);
  }
  .cover {
    position: absolute;
    left: 220px;
    top: 30px;
    width: 760px;
    height: 1140px;
    overflow: hidden;
    font-family: "Josefin Sans", sans-serif;
  }
  .cover-photo {
    position: absolute;
    inset: 0;
    background:
      radial-gradient(ellipse 34% 38% at 50% 92%, var(--photo-shade) 0%, rgba(38,32,40,0.6) 55%, transparent 100%),
      radial-gradient(ellipse 30% 30% at 50% 68%, rgba(90,80,85,0.35), transparent 70%),
      linear-gradient(180deg, var(--photo-top) 0%, var(--photo-mid) 60%, var(--photo-low) 100%);
  }
  .cover-band {
    position: absolute;
    inset: 0;
    width: 760px;
    height: 1140px;
  }
  .cover-text {
    position: absolute;
    left: 0;
    right: 0;
    margin: 0;
    text-align: center;
  }
  .author {
    top: 62px;
    color: var(--white);
    font-weight: 700;
    font-size: 32px;
    letter-spacing: 0.22em;
  }
  .title-lead {
    top: 122px;
    color: var(--cream);
    font-weight: 700;
    font-size: 96px;
    letter-spacing: -0.01em;
    line-height: 1;
  }
  .title-rest {
    top: 214px;
    color: var(--white);
    font-weight: 400;
    font-size: 72px;
    line-height: 78px;
    letter-spacing: -0.01em;
  }
  .subtitle {
    top: 462px;
    color: var(--cream);
    font-weight: 600;
    font-size: 23px;
    line-height: 30px;
    letter-spacing: 0.1em;
  }
  .publisher {
    top: 1062px;
    color: var(--cream);
    font-weight: 600;
    font-size: 24px;
    letter-spacing: 0.12em;
  }
</style>
</head>
<body>
  <main class="cover">
    <div class="cover-photo" role="img" aria-label="Foto: junge Frau mit hellem Tuch und dunklem Gewand hält ein Buch in einem Moscheeinnenraum mit hohen Fenstern"></div>
    <svg class="cover-band" viewBox="0 0 760 1140" aria-hidden="true">
      <polygon points="0,0 760,0 760,560 0,640" fill="var(--cover-blue)"/>
    </svg>
    <p class="cover-text author">LOTTE BRENK</p>
    <h1 class="cover-text title-lead">OH JE,</h1>
    <p class="cover-text title-rest">meine Tage<br>laufen davon<br>weiter</p>
    <p class="cover-text subtitle">Wie du durch kleine Schritte Halt gewinnst<br>- selbst wenn dein Alltag<br>dich stark fordert</p>
    <p class="cover-text publisher">Wald &amp; Stein Verlag</p>
  </main>
</body>
</html>
```